Nice concept website for free living

A website for promoting 2 concepts.

---
Live for free in amsterdam -

homeowner? --- or --- searching to rent?

HOMEOWNER PAGE:

instructions on one page --- homeowners can make x amount in a legal way - and click for more information. Form or contact direct by mobile number.

SEARCHING TO RENT PAGE:

First fill out their details quick form --- Available properties --- show available properties.

Target Market(s)

1. People needing a place to live
2. Homeowners that want more revenue from their real estate

Industry/Entity Type

Tourism

Number of Pages Required

3 page

Requirements
Must have
• Simple nice design
• Homepage quick explanation - what is the concept and choice for
• 1. Homeowners
• 2. Renters
Nice to have
• fresh design

```html
<!DOCTYPE html>
<html lang="en">
<head>
<meta charset="utf-8">
<title>Canalnest – Search for houses to rent across the Netherlands</title>
<link href="https://fonts.googleapis.com/css2?family=Montserrat:wght@500;600;700&family=Open+Sans:wght@400;700&display=swap" rel="stylesheet">
<style>
  :root {
    --white: #ffffff;
    --accent-blue: #1aa3d4;
    --btn-blue-top: #6cc6dd;
    --btn-blue-bottom: #0e93d2;
    --btn-green-top: #d8f23c;
    --btn-green-bottom: #93c91a;
    --footer-bg: #151515;
    --footer-text: #e8e8e8;
    --shade: rgba(0, 0, 0, 0.45);
  }
  * { margin: 0; padding: 0; box-sizing: border-box; }
  html, body { width: 1200px; height: 614px; overflow: hidden; background: #000; }
  .page { position: relative; width: 1200px; height: 614px; overflow: hidden; font-family: "Montserrat", sans-serif; color: var(--white); }

  .hero {
    position: absolute; left: 0; top: 0; width: 1200px; height: 561px;
    background:
      radial-gradient(ellipse 260px 200px at 660px 190px, rgba(236, 170, 70, 0.75), rgba(236, 170, 70, 0) 70%),
      radial-gradient(ellipse 220px 160px at 180px 420px, rgba(170, 40, 90, 0.55), rgba(170, 40, 90, 0) 70%),
      radial-gradient(ellipse 230px 170px at 1020px 420px, rgba(170, 40, 90, 0.55), rgba(170, 40, 90, 0) 70%),
      linear-gradient(180deg, #4a5a66 0%, #6b5a46 30%, #4b3a2c 55%, #2c2622 80%, #1e1c1c 100%);
  }
  .hero::after { content: ""; position: absolute; inset: 0; background: var(--shade); }

  .header { position: absolute; left: 0; top: 0; width: 1200px; height: 120px; }
  .brand { position: absolute; left: 130px; top: 68px; display: flex; align-items: center; gap: 10px; }
  .brand-mark { width: 14px; height: 14px; border: 2px solid var(--white); }
  .brand-name { font-weight: 600; font-size: 23px; letter-spacing: 0.5px; line-height: 1; }

  .main-nav { position: absolute; top: 78px; left: 547px; display: flex; gap: 0; }
  .main-nav a { color: var(--white); text-decoration: none; font-size: 12px; font-weight: 500; letter-spacing: -0.1px; margin-right: 29px; }
  .main-nav a.is-active { color: var(--accent-blue); }

  .intro { position: absolute; left: 0; top: 200px; width: 1200px; text-align: center; }
  .intro-kicker { font-size: 19px; font-weight: 600; letter-spacing: 0.1px; }
  .intro-title { font-size: 58px; font-weight: 700; letter-spacing: 1px; line-height: 1; margin-top: 17px; }
  .intro-text { font-family: "Open Sans", sans-serif; font-size: 11px; font-weight: 700; margin-top: 22px; letter-spacing: 0.2px; }

  .choices { position: absolute; top: 389px; left: 371px; display: flex; gap: 19px; }
  .choice { display: flex; align-items: center; justify-content: center; height: 52px; border-radius: 26px; color: var(--white); text-decoration: none; font-size: 14px; font-weight: 700; letter-spacing: 0.2px; }
  .choice--owner { width: 181px; background: linear-gradient(180deg, var(--btn-blue-top), var(--btn-blue-bottom)); }
  .choice--renter { width: 258px; background: linear-gradient(180deg, var(--btn-green-top), var(--btn-green-bottom)); }

  .slider-arrow { position: absolute; top: 310px; }
  .slider-arrow--prev { left: 82px; }
  .slider-arrow--next { left: 1080px; }

  .footer { position: absolute; left: 0; top: 561px; width: 1200px; height: 53px; background: var(--footer-bg); font-family: "Open Sans", sans-serif; color: var(--footer-text); }
  .footer-legal { position: absolute; left: 133px; top: 19px; font-size: 11px; }
  .footer-legal .sep { margin: 0 9px; }
  .footer-legal a { color: var(--footer-text); text-decoration: none; }
  .social { position: absolute; left: 973px; top: 20px; display: flex; gap: 13px; }
  .social-dot { width: 13px; height: 13px; border-radius: 50%; background: var(--white); }
</style>
</head>
<body>
<div class="page">
  <div class="hero" role="img" aria-label="Photo of an Amsterdam canal at sunset, seen from a bridge with flower boxes and parked bicycles"></div>

  <header class="header">
    <div class="brand">
      <span class="brand-mark"></span>
      <span class="brand-name">CANALNEST</span>
    </div>
    <nav class="main-nav">
      <a class="is-active" href="#">HOME</a>
      <a href="#">ABOUT US</a>
      <a href="#">SERVICES</a>
      <a href="#">FEATURES</a>
      <a href="#">PROPERTY LISTING</a>
      <a href="#">CONTACT US</a>
    </nav>
  </header>

  <svg class="slider-arrow slider-arrow--prev" width="22" height="56" viewBox="0 0 22 56" aria-hidden="true">
    <polyline points="20,2 2,28 20,54" fill="none" stroke="rgba(255,255,255,0.7)" stroke-width="2"/>
  </svg>
  <svg class="slider-arrow slider-arrow--next" width="22" height="56" viewBox="0 0 22 56" aria-hidden="true">
    <polyline points="2,2 20,28 2,54" fill="none" stroke="rgba(255,255,255,0.7)" stroke-width="2"/>
  </svg>

  <section class="intro">
    <p class="intro-kicker">SEARCH FOR HOUSES TO RENT ACROSS</p>
    <h1 class="intro-title">THE NETHERLANDS</h1>
    <p class="intro-text">LOREM IPSUM DOLOR SIT AMET, CONSECTETUR ADIPISCING ELIT</p>
  </section>

  <div class="choices">
    <a class="choice choice--owner" href="#">HOMEOWNER</a>
    <a class="choice choice--renter" href="#">SEARCHING TO RENT?</a>
  </div>

  <footer class="footer">
    <p class="footer-legal">© 2016 Canalnest. All rights reserved.<span class="sep">|</span><a href="#">privacy policy</a></p>
    <div class="social">
      <span class="social-dot"></span>
      <span class="social-dot"></span>
      <span class="social-dot"></span>
      <span class="social-dot"></span>
    </div>
  </footer>
</div>
</body>
</html>
```